Legal Service Estimated Retainer and Average Case Value

We need an 11x14 flyer that contains the standard retainers and average cost be case, both provided in documents, for each case type we handle. We need the information displayed, preferably in a way that makes the information readable but less troubling to a client shocked at price of litigation. We need one sheet with the retainers and average case value merged into one table.

Target Market(s)

Potential Clients

Font styles to use
Serif
Sans Serif

```html
<!DOCTYPE html>
<html lang="en">
<head>
<meta charset="utf-8">
<title>Fee Per Case Type</title>
<link rel="stylesheet" href="https://fonts.googleapis.com/css2?family=Cinzel:wght@500;600&family=Lato:wght@400;700&display=swap">
<style>
  :root {
    --navy-deep: #1b1d36;
    --navy: #15194a;
    --navy-mist: #2a2d4c;
    --white: #ffffff;
    --row-alt: #f1f1f3;
    --ink-soft: #58595f;
    --photo-warm: #b98d6c;
    --photo-cool: #7d8a8c;
  }
  * { margin: 0; padding: 0; box-sizing: border-box; }
  html, body { width: 943px; height: 1200px; overflow: hidden; }
  body {
    position: relative;
    background:
      radial-gradient(ellipse at 30% 75%, rgba(70,72,100,0.45), transparent 60%),
      linear-gradient(180deg, var(--navy-deep) 0%, var(--navy-mist) 45%, var(--navy-deep) 100%);
    font-family: 'Lato', sans-serif;
    color: var(--white);
  }
  .brand {
    position: absolute; left: 82px; top: 86px;
    display: flex; align-items: center; gap: 12px;
    font-family: 'Cinzel', serif; font-weight: 500; color: var(--white);
  }
  .brand-mark { width: 14px; height: 14px; background: var(--white); }
  .brand-name { line-height: 1; }
  .brand-name small { display: block; font-size: 12px; letter-spacing: 0.5px; margin-bottom: 3px; }
  .brand-name span { display: block; font-size: 26px; letter-spacing: 0.5px; }
  .title {
    position: absolute; left: 93px; top: 206px;
    font-family: 'Cinzel', serif; font-weight: 600;
    font-size: 52px; line-height: 47px; letter-spacing: 1px;
  }
  .intro {
    position: absolute; left: 92px; top: 336px; width: 475px;
    font-size: 18.6px; line-height: 24px;
  }
  .portrait { position: absolute; left: 553px; top: 20px; width: 373px; height: 460px; }
  .fee-table {
    position: absolute; left: 81px; top: 521px; width: 794px; height: 627px;
    background: var(--white);
  }
  .col-head {
    position: absolute; top: 0; height: 27px;
    background: var(--navy); color: var(--white);
    font-weight: 700; font-size: 18px; line-height: 27px; text-align: center;
  }
  .col-head.fee { left: 466px; width: 190px; }
  .col-head.retainer { left: 664px; width: 113px; }
  .rows { position: absolute; top: 38px; left: 0; right: 0; list-style: none; }
  .row {
    display: grid; grid-template-columns: 466px 190px 138px;
    height: 44.5px; align-items: center;
    color: var(--ink-soft); font-size: 18px;
  }
  .row:nth-child(odd) { background: var(--row-alt); height: 34.5px; }
  .row .case { padding-left: 33px; white-space: nowrap; letter-spacing: -0.1px; }
  .row .fee, .row .retainer { text-align: center; }
  .row .retainer { padding-right: 26px; }
</style>
</head>
<body>
  <header class="brand">
    <div class="brand-mark"></div>
    <div class="brand-name"><small>The Law Office of</small><span>Daniel M Whitfield</span></div>
  </header>

  <h1 class="title">Fee Per<br>Case Type</h1>

  <p class="intro">In order for our clients to set expectations for legal fees, we provide the national average range of fees per case type. These are only to provide you with an understanding of what other cases have cost clients in similar cases. Please note these are not estimates nor guarantees of your own legal costs.</p>

  <svg class="portrait" viewBox="0 0 373 460" role="img" aria-label="Shield-shaped photo of a smiling couple embracing outdoors">
    <defs>
      <linearGradient id="portraitTone" x1="0" y1="0" x2="1" y2="1">
        <stop offset="0" stop-color="var(--photo-cool)"/>
        <stop offset="0.5" stop-color="var(--photo-warm)"/>
        <stop offset="1" stop-color="#8a6f64"/>
      </linearGradient>
    </defs>
    <path d="M0 0 H373 V180 C373 320 275 410 186 460 C98 410 0 320 0 180 Z" fill="url(#portraitTone)"/>
  </svg>

  <section class="fee-table">
    <div class="col-head fee">Average Fee</div>
    <div class="col-head retainer">Retainer</div>
    <ul class="rows">
      <li class="row"><span class="case">Divorce (3301 C)</span><span class="fee">$1,500 - $3,000</span><span class="retainer">$2,000</span></li>
      <li class="row"><span class="case">Divorce (3301 D)</span><span class="fee">$2,000 - $3,000</span><span class="retainer">$2,500</span></li>
      <li class="row"><span class="case">Custody Initial Order</span><span class="fee">$4,000 - $7,000</span><span class="retainer">$3,000</span></li>
      <li class="row"><span class="case">Custody Contempt/Modification</span><span class="fee">$5,000 - $8,000</span><span class="retainer">$3,500</span></li>
      <li class="row"><span class="case">Custody &amp; Support</span><span class="fee">$5,000 - $8,000</span><span class="retainer">$3,000</span></li>
      <li class="row"><span class="case">Divorce &amp; Support</span><span class="fee">$2,000 - $4,000</span><span class="retainer">$3,000</span></li>
      <li class="row"><span class="case">Divorce &amp; Custody</span><span class="fee">$5,000 - $8,000</span><span class="retainer">$3,500</span></li>
      <li class="row"><span class="case">Divorce &amp; Equitable Distribution</span><span class="fee">$6,000 - $10,000</span><span class="retainer">$3,500</span></li>
      <li class="row"><span class="case">Divorce, Custody &amp; Support</span><span class="fee">$8,000 - $12,000</span><span class="retainer">$3,500</span></li>
      <li class="row"><span class="case">Divorce, Equitable Distribution &amp; Custody</span><span class="fee">$10,000 - $15,000</span><span class="retainer">$5,000</span></li>
      <li class="row"><span class="case">Divorce, Equitable Distribution &amp; Support</span><span class="fee">$8,000 - $12,000</span><span class="retainer">$3,500</span></li>
      <li class="row"><span class="case">Divorce, Equitable Distribution, Custody &amp; Support</span><span class="fee">$12,000 - $15,000</span><span class="retainer">$3,500</span></li>
      <li class="row"><span class="case">Protection from Abuse</span><span class="fee">$1,500 - $3,000</span><span class="retainer">$2,000</span></li>
    </ul>
  </section>
</body>
</html>
```